VM Tarlo Agency

we need a design for panel, cm 235 x 184 height + roll up as attached sizes, attached find also my logo, my company is www.vmtarloagency.com

Industry/Entity Type

Freight Forwarding

```html
<!DOCTYPE html>
<html lang="en">
<head>
<meta charset="UTF-8">
<title>VM Tarlo Agency – Exhibition Panel</title>
<link href="https://fonts.googleapis.com/css2?family=Oswald:wght@500;600&family=Open+Sans:wght@400;600;700&display=swap" rel="stylesheet">
<style>
  :root {
    --navy: #1d2a5c;
    --red: #c8161d;
    --paper: #f2f3f5;
    --paper-edge: #e4e6ea;
    --sky: #8fb4cf;
    --steel: #b9c6d2;
    --white: #ffffff;
  }
  * { box-sizing: border-box; margin: 0; padding: 0; }
  html, body { width: 1200px; height: 1063px; overflow: hidden; }
  body {
    background: linear-gradient(180deg, var(--white) 0%, var(--paper) 55%, var(--paper-edge) 100%);
    font-family: "Open Sans", sans-serif;
    position: relative;
  }
  .panel { position: absolute; inset: 0; }

  .brand { position: absolute; left: 79px; top: 145px; display: flex; align-items: center; gap: 18px; }
  .brand-dot { width: 74px; height: 74px; border-radius: 50%; background: var(--navy); flex: none; }
  .brand-name {
    font-family: "Oswald", sans-serif; font-weight: 600; font-size: 58px; line-height: 1;
    color: var(--navy); text-transform: uppercase; letter-spacing: -0.5px;
  }
  .brand-tagline {
    font-family: "Oswald", sans-serif; font-weight: 500; font-size: 32px; line-height: 1.1;
    color: var(--red); margin-top: 6px; letter-spacing: 0.5px;
  }

  .headline {
    position: absolute; left: 745px; top: 140px; width: 400px; text-align: center;
    font-family: "Oswald", sans-serif; font-weight: 600; font-size: 42px; line-height: 1.22;
    color: var(--navy); text-transform: uppercase;
  }

  .hero-visual {
    position: absolute; left: 0; top: 281px; width: 720px; height: 640px;
    background:
      radial-gradient(ellipse at 30% 55%, rgba(224,170,40,0.55) 0%, rgba(224,170,40,0) 38%),
      radial-gradient(ellipse at 68% 55%, rgba(196,95,50,0.45) 0%, rgba(196,95,50,0) 35%),
      radial-gradient(ellipse at 50% 30%, rgba(143,180,207,0.75) 0%, rgba(143,180,207,0) 65%),
      linear-gradient(90deg, rgba(143,180,207,0.6) 0%, rgba(185,198,210,0.35) 70%, rgba(242,243,245,0) 100%);
  }

  .services { position: absolute; left: 735px; top: 330px; width: 420px; }
  .service-grid { display: grid; grid-template-columns: repeat(3, 140px); row-gap: 32px; }
  .service { display: flex; flex-direction: column; align-items: center; }
  .service-icon {
    width: 82px; height: 82px; border-radius: 50%; background: var(--white);
    border: 4px solid var(--navy); display: flex; align-items: center; justify-content: center;
    box-shadow: 0 6px 12px rgba(0,0,0,0.18);
  }
  .service-icon svg { width: 44px; height: 44px; fill: var(--red); }
  .service-label {
    margin-top: 12px; font-size: 14px; font-weight: 700; color: var(--navy);
    text-transform: uppercase; white-space: nowrap;
  }

  .quote { position: absolute; left: 782px; top: 692px; width: 344px; text-align: center; }
  .quote-lead { font-size: 16px; font-weight: 700; color: var(--navy); text-transform: uppercase; }
  .quote-url {
    display: block; margin-top: 16px; height: 56px; line-height: 56px; border-radius: 28px;
    background: var(--red); color: var(--white); font-size: 24px; font-weight: 400;
    box-shadow: 0 4px 8px rgba(0,0,0,0.2);
  }

  .footer-bands { position: absolute; left: 0; top: 0; width: 1200px; height: 1063px; }
  .contact {
    position: absolute; right: 86px; top: 942px; text-align: right; color: var(--white);
    font-size: 16px; line-height: 1.5; text-transform: uppercase;
  }
  .contact-phone { margin-bottom: 18px; }
</style>
</head>
<body>
<main class="panel">

  <div class="hero-visual" role="img" aria-label="Freight montage: cargo plane over a faint world map and city skyline, yellow locomotive and container truck"></div>

  <svg class="footer-bands" viewBox="0 0 1200 1063" aria-hidden="true">
    <polygon points="0,900 540,975 0,1063" fill="var(--red)"/>
    <polygon points="0,1063 0,1052 1200,840 1200,1063" fill="var(--navy)"/>
  </svg>

  <header class="brand">
    <span class="brand-dot"></span>
    <div>
      <div class="brand-name">VM Tarlo Agency</div>
      <div class="brand-tagline">Shipping and Logistics</div>
    </div>
  </header>

  <h1 class="headline">We make your business<br>flow continously</h1>

  <section class="services">
    <div class="service-grid">
      <div class="service">
        <div class="service-icon"><svg viewBox="0 0 24 24"><path d="M2 12.5h8l3-6h2l-1.5 6H20l2-2h1l-1 3 1 3h-1l-2-2h-6.5L15 20.5h-2l-3-6H2z"/></svg></div>
        <div class="service-label">Air Freight</div>
      </div>
      <div class="service">
        <div class="service-icon"><svg viewBox="0 0 24 24"><path d="M8 4h8v4h3v4l2 1-3 7H6l-3-7 2-1V8h3z"/></svg></div>
        <div class="service-label">Sea Freight</div>
      </div>
      <div class="service">
        <div class="service-icon"><svg viewBox="0 0 24 24"><path d="M6 3h12v12H6zM5 16h14v3h-2v2h-3v-2h-4v2H7v-2H5z"/></svg></div>
        <div class="service-label">Land Freight</div>
      </div>
      <div class="service">
        <div class="service-icon"><svg viewBox="0 0 24 24"><path d="M7 2h10l2 3v11l-2 2H7l-2-2V5zM7 6v5h10V6zM6 20h3l-2 2H5zm9 0h3l1 2h-2z"/></svg></div>
        <div class="service-label">Rail Services</div>
      </div>
      <div class="service">
        <div class="service-icon"><svg viewBox="0 0 24 24"><path d="M4 3h3l4 13h9v2H10L6 5H4zM10 7h8v7h-6zM10 21a2 2 0 1 0 .1 0z"/></svg></div>
        <div class="service-label">Project Cargo</div>
      </div>
      <div class="service">
        <div class="service-icon"><svg viewBox="0 0 24 24"><path d="M12 2 2 8v14h3V11h14v11h3V8zM7 13h10v3H7zm0 4h10v3H7z"/></svg></div>
        <div class="service-label">Warehouse</div>
      </div>
    </div>
  </section>

  <section class="quote">
    <p class="quote-lead">Contact us for a free quote</p>
    <span class="quote-url">www.vmtarloagency.com</span>
  </section>

  <footer class="contact">
    <p class="contact-phone">Phone: +39 0255510873</p>
    <p>Headquarter: Via G. Verdi 21</p>
    <p>20121 Lorenza-Milan-Italy</p>
  </footer>

</main>
</body>
</html>
```